Upscale neighbourhood mail campaign requiring 3 postcard designs

I am looking for a series of 3 postcards to be designed. They all must have a common look to them to show they belong to the same company. We are a local real estate company that specializes in an area called Hollowby Ridge. You can visit our website at www.hollowbyridgehomes.ca to have a peek. I have HD photos I can provide of the area, or include your own ideas/images. The post cards text will be provided and they will be sent as unaddressed admail, meaning there is no need to include areas for postage or mailing addresses. The final design should be clean, recognizable and professional. These cards must have visual impact on the recipients.

COPY for 3 POSTCARDs

POSTCARD 1

FRONT

(included Logo)

Get noticed.
Your home deserves it

BACK

We take finding Buyers for your home very seriously.

Through our unique, Hollowby Ridge specific website, targeted digital marketing, EXCLUSIVE Buyer incentives and our featured listing promotion, your home is in front of the people that want to see it. People who WANT to live in Hollowby Ridge.

Visit hollowbyridgehomes.ca to learn more about what we do so your home can GET NOTICED. Your home deserves it.

Tobias Hallworth- PREC | Pellston Realty LTD | 604-555-0182 | homes@hallworth-example.ca

This communication is not intended to cause or induce breach of an existing agency agreement. Although this information has been received from sources deemed reliable, we assume no responsibility for its accuracy and without offering advice, make this submission to prior sale or lease, change in price or terms, and withdrawal without notice

POSTCARD 2

FRONT

Logo

Get noticed.
Expect the best.

BACK

You deserve the best when it comes to the marketing and exposure of your home, which is why your neighbours choose hollowbyridgehomes.ca to sell their home. Our award winning results combined with our systematized approach to marketing makes selling your home with us a breeze. In addition, you have full access to our dedicated client concierge, in place to ensure your sale is stress free and an overall rewarding experience.

Visit hollowbyridgehomes.ca to learn more about what we do so your home can GET NOTICED. Expect the best.

POSTCARD 3

FRONT

Logo

Get noticed.
Rule the web

BACK

No one promotes your home more than hollowbyridgehomes.ca. Just try us. Type hollowby ridge homes into any internet search browser and see for yourself. We advertise Hollowby Ridge internationally, in all major Canadian Cities and locally to affluent Buyers who appreciate what Hollowby Ridge has to offer. No one offers a more specific, targeted approach to getting your home sold.

Visit hollowbyridgehomes.ca to learn more about what we do so your home can GET NOTICED so you can rule the web.

Target Market(s)

Upscale neighbourhood in Surrey BC, Canada called Hollowby Ridge

Industry/Entity Type

Real Estate

Other font styles liked:
• Lato

Colors

Designer to choose colors to be used in the design.

Requirements
Must have
• -Clean, impactful and professional looking card
• -Font- Lato
• -Provided Hollowby Ridge Homes logo
• -Check www.hollowbyridgehomes.ca for complimentary color scheme
• -provided Hollowby Ridge logo on the front
• -provided --TH logo, Pellston Realty logo and medallion crest on the back
• -Disclaimer in small, low-key font/color - "This communication is not intended to cause or induce breach of an existing agency agreement. Although this information has been received from sources deemed reliable, we assume no responsibility for its accuracy and without offering advice, make this submission to prior sale or lease, change in price or terms, and withdrawal without notice"
Nice to have
• -bold images, not 100% necessary though (discretion of designer)
• -impactful front of postcard
Should not have
• -cartoon style drawings
• -areas for postage or mailing addresses (this will be sent as non addressed admail by the local postal courier)

```html
<!DOCTYPE html>
<html lang="en">
<head>
<meta charset="utf-8">
<title>Hollowby Ridge Homes – Postcard Series</title>
<link href="https://fonts.googleapis.com/css2?family=Cinzel:wght@500;600&family=Lato:wght@400;700&family=Montserrat:wght@500;600&display=swap" rel="stylesheet">
<style>
  :root{
    --stage:#d5d5d5;
    --green:#5f6b2b;
    --green-soft:#6c7836;
    --charcoal:#333333;
    --charcoal-2:#3a3a3a;
    --white:#ffffff;
    --ink:#2b2b2b;
    --muted:#e4e6d8;
    --sky:#9cc3e4;
    --lawn:#6d9a3c;
  }
  *{margin:0;padding:0;box-sizing:border-box}
  html,body{width:1200px;height:1200px;overflow:hidden;background:var(--stage)}
  .sheet{position:relative;width:1200px;height:1200px;background:var(--stage)}
  .card{position:absolute;width:503px;height:325px;overflow:hidden;background:var(--white);
        box-shadow:0 3px 6px rgba(0,0,0,.28)}
  .abs{position:absolute}

  /* ---------- front ---------- */
  .brand-panel{left:0;top:0;width:156px;height:207px;background:linear-gradient(160deg,#3c3c3c,#2c2c2c)}
  .brand{left:0;top:78px;width:156px;text-align:center;color:var(--white);font-family:"Cinzel",serif}
  .brand-mark{display:block;width:22px;height:22px;border:2px solid var(--white);margin:0 auto 8px}
  .brand-name{font-size:13px;font-weight:500;letter-spacing:.3px;line-height:1}
  .brand-sub{font-size:8px;font-weight:500;letter-spacing:3px;margin-top:2px;line-height:1}
  .photo{background:linear-gradient(180deg,var(--sky) 0%,#b9c7c9 35%,#5b6f8f 55%,var(--lawn) 78%,#5c8a30 100%)}
  .front .photo{left:156px;top:0;width:347px;height:203px}
  .photo-rule{left:74px;top:202px;width:429px;height:3px;background:var(--white)}
  .headline-band{left:0;top:207px;width:503px;height:39px;background:var(--green);
        color:var(--white);font-family:"Cinzel",serif;font-weight:600;font-size:32px;
        text-align:center;line-height:39px;letter-spacing:.5px}
  .headline-band .small{font-size:26px}
  .tagline{left:0;top:250px;width:503px;text-align:center;font-family:"Lato",sans-serif;
        font-weight:700;font-size:23px;color:var(--green);line-height:1.1}
  .realty{left:0;top:283px;width:503px;display:flex;align-items:center;gap:8px;padding:0 0}
  .realty .rule{flex:1;height:2px;background:var(--green)}
  .realty .label{font-family:"Montserrat",sans-serif;font-weight:600;font-size:9.5px;letter-spacing:.6px;color:var(--ink)}
  .contact-bar{left:0;top:298px;width:503px;height:27px;background:var(--charcoal);
        display:flex;justify-content:center;align-items:center;gap:34px;
        color:var(--white);font-family:"Montserrat",sans-serif;font-weight:600;font-size:9.5px}
  .contact-bar span,.agent-line{display:flex;align-items:center;gap:4px}
  .ico{width:8px;height:8px;fill:none;stroke:currentColor;stroke-width:1.4}

  /* ---------- back ---------- */
  .back{width:504px}
  .copy-panel{left:0;top:0;width:252px;height:221px;background:var(--green)}
  .copy-head{left:18px;top:12px;width:220px;color:var(--white);font-family:"Montserrat",sans-serif;
        font-weight:500;font-size:12.5px;line-height:1.15}
  .copy-box{left:0;top:44px;width:262px;height:88px;background:var(--charcoal-2);padding:14px 14px 0 14px;
        color:var(--white);font-family:"Lato",sans-serif;font-size:7.2px;line-height:1.35}
  .copy-box b{font-size:9.5px;font-weight:700}
  .copy-box .smallcaps{font-family:"Cinzel",serif;font-size:8px;letter-spacing:.5px;margin-top:6px;display:block}
  .body{color:var(--white);font-family:"Lato",sans-serif;font-size:7.2px;line-height:1.35;text-align:justify}
  .disclaimer{color:var(--muted)}
  .section-title{font-family:"Cinzel",serif;font-weight:500;font-size:16px;color:var(--white);letter-spacing:.4px}
  .lower-rule{left:0;top:220px;width:170px;height:3px;background:var(--white)}
  .back .lower-photo{left:0;top:223px;width:252px;height:102px}
  .visit{left:252px;top:0;width:252px;height:104px;padding:10px 0 0 30px;background:var(--white)}
  .visit-title{font-family:"Cinzel",serif;font-size:12px;color:var(--ink);font-weight:500;
        border-bottom:1.5px solid var(--green);display:inline-block;padding-bottom:1px}
  .visit-url{font-family:"Montserrat",sans-serif;font-weight:600;font-size:11.5px;color:var(--green);
        margin-top:5px;display:flex;align-items:center;gap:4px}
  .visit-note{font-family:"Lato",sans-serif;font-size:7px;color:var(--ink);margin-top:4px}
  .visit-head{font-family:"Cinzel",serif;font-weight:600;font-size:18px;color:var(--green);margin-top:6px;line-height:1}
  .visit-tag{font-family:"Lato",sans-serif;font-weight:700;font-size:12.5px;color:var(--charcoal);margin-top:4px}
  .back .street-photo{left:252px;top:104px;width:252px;height:131px;
        background:linear-gradient(180deg,#a9cde9 0%,#c8d8de 30%,#8f8a7c 52%,#6e9f3e 70%,#b9b7b0 100%)}
  .agent{left:252px;top:235px;width:252px;height:90px;background:var(--charcoal);padding:9px 0 0 16px;color:var(--white)}
  .agent-name{font-family:"Montserrat",sans-serif;font-weight:600;font-size:10px}
  .agent-firm{font-family:"Montserrat",sans-serif;font-weight:600;font-size:7px;margin-top:3px;display:flex;align-items:center;gap:6px}
  .agent-firm .rule{width:88px;height:1px;background:var(--white)}
  .agent-line{font-family:"Montserrat",sans-serif;font-size:8px;margin-top:4px}
  .agent-brand{left:164px;top:49px;width:80px;text-align:center;font-family:"Cinzel",serif;color:var(--white)}
  .agent-brand .brand-mark{width:14px;height:14px;border-width:1.5px;margin-bottom:3px}
  .agent-brand .brand-name{font-size:7px}
  .agent-brand .brand-sub{font-size:5px;letter-spacing:2px}
</style>
</head>
<body>
<main class="sheet">

  <!-- ===== Front cards ===== -->
  <section class="card front" style="left:66px;top:48px">
    <div class="abs brand-panel"></div>
    <div class="abs brand"><span class="brand-mark"></span><div class="brand-name">HOLLOWBY RIDGE</div><div class="brand-sub">HOMES.CA</div></div>
    <div class="abs photo" role="img" aria-label="Photo of a navy craftsman-style house with white trim and a green lawn"></div>
    <div class="abs photo-rule"></div>
    <h2 class="abs headline-band">G<span class="small">ET</span> N<span class="small">OTICED</span></h2>
    <p class="abs tagline">Your home deserves it</p>
    <div class="abs realty"><span class="rule"></span><span class="label">PELLSTON REALTY</span><span class="rule"></span></div>
    <div class="abs contact-bar">
      <span><svg class="ico" viewBox="0 0 10 10"><path d="M2 1l2 2-1 1.5a6 6 0 0 0 2.5 2.5L7 6l2 2-1.5 1.5C5 9 1 5 .5 2z"/></svg>604.555.0182</span>
      <span><svg class="ico" viewBox="0 0 10 10"><circle cx="5" cy="5" r="4"/><path d="M1 5h8"/></svg>www.hollowbyridgehomes.ca</span>
      <span><svg class="ico" viewBox="0 0 10 10"><rect x="1" y="2" width="8" height="6"/><path d="M1 2l4 3 4-3"/></svg>homes@hallworth-example.ca</span>
    </div>
  </section>

  <section class="card front" style="left:66px;top:427px">
    <div class="abs brand-panel"></div>
    <div class="abs brand"><span class="brand-mark"></span><div class="brand-name">HOLLOWBY RIDGE</div><div class="brand-sub">HOMES.CA</div></div>
    <div class="abs photo" role="img" aria-label="Photo of a navy craftsman-style house with white trim and a green lawn"></div>
    <div class="abs photo-rule"></div>
    <h2 class="abs headline-band">G<span class="small">ET</span> N<span class="small">OTICED</span></h2>
    <p class="abs tagline">Expect the best</p>
    <div class="abs realty"><span class="rule"></span><span class="label">PELLSTON REALTY</span><span class="rule"></span></div>
    <div class="abs contact-bar">
      <span><svg class="ico" viewBox="0 0 10 10"><path d="M2 1l2 2-1 1.5a6 6 0 0 0 2.5 2.5L7 6l2 2-1.5 1.5C5 9 1 5 .5 2z"/></svg>604.555.0182</span>
      <span><svg class="ico" viewBox="0 0 10 10"><circle cx="5" cy="5" r="4"/><path d="M1 5h8"/></svg>www.hollowbyridgehomes.ca</span>
      <span><svg class="ico" viewBox="0 0 10 10"><rect x="1" y="2" width="8" height="6"/><path d="M1 2l4 3 4-3"/></svg>homes@hallworth-example.ca</span>
    </div>
  </section>

  <section class="card front" style="left:66px;top:815px">
    <div class="abs brand-panel"></div>
    <div class="abs brand"><span class="brand-mark"></span><div class="brand-name">HOLLOWBY RIDGE</div><div class="brand-sub">HOMES.CA</div></div>
    <div class="abs photo" role="img" aria-label="Photo of a navy craftsman-style house with white trim and a green lawn"></div>
    <div class="abs photo-rule"></div>
    <h2 class="abs headline-band">G<span class="small">ET</span> N<span class="small">OTICED</span></h2>
    <p class="abs tagline">Rule the web</p>
    <div class="abs realty"><span class="rule"></span><span class="label">PELLSTON REALTY</span><span class="rule"></span></div>
    <div class="abs contact-bar">
      <span><svg class="ico" viewBox="0 0 10 10"><path d="M2 1l2 2-1 1.5a6 6 0 0 0 2.5 2.5L7 6l2 2-1.5 1.5C5 9 1 5 .5 2z"/></svg>604.555.0182</span>
      <span><svg class="ico" viewBox="0 0 10 10"><circle cx="5" cy="5" r="4"/><path d="M1 5h8"/></svg>www.hollowbyridgehomes.ca</span>
      <span><svg class="ico" viewBox="0 0 10 10"><rect x="1" y="2" width="8" height="6"/><path d="M1 2l4 3 4-3"/></svg>homes@hallworth-example.ca</span>
    </div>
  </section>

  <!-- ===== Back cards ===== -->
  <section class="card back" style="left:618px;top:48px">
    <div class="abs copy-panel"></div>
    <h3 class="abs copy-head">We take finding Buyers<br>for your home very seriously</h3>
    <div class="abs copy-box">
      Through our unique, Hollowby Ridge specific website, targeted digital marketing,<br>
      <b>EXCLUSIVE</b> Buyer incentives and our featured listing promotion, your home is in front of the people that want to see it.
      <span class="smallcaps">People who want to live in <b style="font-family:'Montserrat',sans-serif;font-size:8px">Hollowby Ridge</b></span>
    </div>
    <p class="abs body disclaimer" style="left:16px;top:144px;width:222px">This communication is not intended to cause or induce breach of an existing agency agreement. Although this information has been received from sources deemed reliable, we assume no responsibility for its accuracy and without offering advice, make this submission to prior sale or lease, change in price or terms, and withdrawal without notice</p>
    <div class="abs lower-rule"></div>
    <div class="abs photo lower-photo" role="img" aria-label="Photo of a single-storey home with a hipped roof and landscaped garden"></div>
    <div class="abs visit">
      <div class="visit-title">Visit us</div>
      <div class="visit-url"><svg class="ico" viewBox="0 0 10 10"><circle cx="5" cy="5" r="4"/><path d="M1 5h8"/></svg>hollowbyridgehomes.ca</div>
      <div class="visit-note">to learn more about what we do so your home can</div>
      <div class="visit-head">GET NOTICED</div>
      <div class="visit-tag">Your home deserves it</div>
    </div>
    <div class="abs street-photo" role="img" aria-label="Photo of a curving residential street lined with houses and lawns"></div>
    <div class="abs agent">
      <div class="agent-name">Tobias Hallworth- PREC</div>
      <div class="agent-firm">Pellston Realty LTD <span class="rule"></span></div>
      <div class="agent-line"><svg class="ico" viewBox="0 0 10 10"><path d="M2 1l2 2-1 1.5a6 6 0 0 0 2.5 2.5L7 6l2 2-1.5 1.5C5 9 1 5 .5 2z"/></svg>604.555.0182</div>
      <div class="agent-line"><svg class="ico" viewBox="0 0 10 10"><rect x="1" y="2" width="8" height="6"/><path d="M1 2l4 3 4-3"/></svg>homes@hallworth-example.ca</div>
      <div class="agent-line"><svg class="ico" viewBox="0 0 10 10"><circle cx="5" cy="5" r="4"/><path d="M1 5h8"/></svg>www.hollowbyridgehomes.ca</div>
      <div class="abs agent-brand"><span class="brand-mark"></span><div class="brand-name">HOLLOWBY RIDGE</div><div class="brand-sub">HOMES.CA</div></div>
    </div>
  </section>

  <section class="card back" style="left:618px;top:427px">
    <div class="abs copy-panel"></div>
    <h3 class="abs section-title" style="left:14px;top:38px">You deserve the best</h3>
    <p class="abs body" style="left:14px;top:64px;width:224px">when it comes to the marketing and exposure of your home, which is why your neighbours choose hollowbyridgehomes.ca to sell their home. Our award winning results combined with our systematized approach to marketing makes selling your home with us a breeze. In addition, you have full access to our</p>
    <p class="abs body disclaimer" style="left:14px;top:124px;width:224px">This communication is not intended to cause or induce breach of an existing agency agreement. Although this information has been received from sources deemed reliable, we assume no responsibility for its accuracy and without offering advice, make this submission to prior sale or lease, change in price or terms, and withdrawal without notice</p>
    <div class="abs lower-rule"></div>
    <div class="abs photo lower-photo" role="img" aria-label="Photo of a single-storey home with a hipped roof and landscaped garden"></div>
    <div class="abs visit">
      <div class="visit-title">Visit us</div>
      <div class="visit-url"><svg class="ico" viewBox="0 0 10 10"><circle cx="5" cy="5" r="4"/><path d="M1 5h8"/></svg>hollowbyridgehomes.ca</div>
      <div class="visit-note">to learn more about what we do so your home can</div>
      <div class="visit-head">GET NOTICED</div>
      <div class="visit-tag">Your home deserves it</div>
    </div>
    <div class="abs street-photo" role="img" aria-label="Photo of a curving residential street lined with houses and lawns"></div>
    <div class="abs agent">
      <div class="agent-name">Tobias Hallworth- PREC</div>
      <div class="agent-firm">Pellston Realty LTD <span class="rule"></span></div>
      <div class="agent-line"><svg class="ico" viewBox="0 0 10 10"><path d="M2 1l2 2-1 1.5a6 6 0 0 0 2.5 2.5L7 6l2 2-1.5 1.5C5 9 1 5 .5 2z"/></svg>604.555.0182</div>
      <div class="agent-line"><svg class="ico" viewBox="0 0 10 10"><rect x="1" y="2" width="8" height="6"/><path d="M1 2l4 3 4-3"/></svg>homes@hallworth-example.ca</div>
      <div class="agent-line"><svg class="ico" viewBox="0 0 10 10"><circle cx="5" cy="5" r="4"/><path d="M1 5h8"/></svg>www.hollowbyridgehomes.ca</div>
      <div class="abs agent-brand"><span class="brand-mark"></span><div class="brand-name">HOLLOWBY RIDGE</div><div class="brand-sub">HOMES.CA</div></div>
    </div>
  </section>

  <section class="card back" style="left:618px;top:815px">
    <div class="abs copy-panel"></div>
    <h3 class="abs" style="left:14px;top:20px;color:var(--white);font-family:'Montserrat',sans-serif;font-weight:600;font-size:12.5px">No one promotes your home</h3>
    <p class="abs" style="left:14px;top:36px;color:var(--white);font-family:'Montserrat',sans-serif;font-weight:600;font-size:7px">more than hollowbyridgehomes.ca.</p>
    <h3 class="abs section-title" style="left:14px;top:50px;font-size:17px">Just try us.</h3>
    <p class="abs body" style="left:14px;top:77px;width:224px">Type hollowby ridge homes into any internet search browser and see for yourself. We advertise Hollowby Ridge internationally, in all major Canadian Cities and locally to affluent Buyers who appreciate what Hollowby Ridge has to offer. No one offers a more specific, targeted approach to getting your home sold.</p>
    <p class="abs body disclaimer" style="left:14px;top:140px;width:224px">This communication is not intended to cause or induce breach of an existing agency agreement. Although this information has been received from sources deemed reliable, we assume no responsibility for its accuracy and without offering advice, make this submission to prior sale or lease, change in price or terms, and withdrawal without notice</p>
    <div class="abs lower-rule"></div>
    <div class="abs photo lower-photo" role="img" aria-label="Photo of a single-storey home with a hipped roof and landscaped garden"></div>
    <div class="abs visit">
      <div class="visit-title">Visit us</div>
      <div class="visit-url"><svg class="ico" viewBox="0 0 10 10"><circle cx="5" cy="5" r="4"/><path d="M1 5h8"/></svg>hollowbyridgehomes.ca</div>
      <div class="visit-note">to learn more about what we do so your home can</div>
      <div class="visit-head">GET NOTICED</div>
      <div class="visit-tag">Your home deserves it</div>
    </div>
    <div class="abs street-photo" role="img" aria-label="Photo of a curving residential street lined with houses and lawns"></div>
    <div class="abs agent">
      <div class="agent-name">Tobias Hallworth- PREC</div>
      <div class="agent-firm">Pellston Realty LTD <span class="rule"></span></div>
      <div class="agent-line"><svg class="ico" viewBox="0 0 10 10"><path d="M2 1l2 2-1 1.5a6 6 0 0 0 2.5 2.5L7 6l2 2-1.5 1.5C5 9 1 5 .5 2z"/></svg>604.555.0182</div>
      <div class="agent-line"><svg class="ico" viewBox="0 0 10 10"><rect x="1" y="2" width="8" height="6"/><path d="M1 2l4 3 4-3"/></svg>homes@hallworth-example.ca</div>
      <div class="agent-line"><svg class="ico" viewBox="0 0 10 10"><circle cx="5" cy="5" r="4"/><path d="M1 5h8"/></svg>www.hollowbyridgehomes.ca</div>
      <div class="abs agent-brand"><span class="brand-mark"></span><div class="brand-name">HOLLOWBY RIDGE</div><div class="brand-sub">HOMES.CA</div></div>
    </div>
  </section>

</main>
</body>
</html>
```